Meatball Posters

We are opening a Meatball Sandwich Shop called
Orvin's Legendary Slider Shack. It is a quirky concept with a fun, casual, and sometime mildly inappropriate theme.
Sandwiches Like
"Saucy Rounds" Blue Cheese Bacon Meatball Sandwich
"Caramba" Tex Mex Meatball Sandwich
"Nonna's Last Word" Classic Meatball Sandwich
You get the idea......We are covering the interior of the place with posters of different meatball things.....That is where this comes in. I am looking for fun, quirky posters that incorporate meatballs. Think along the lines of the movie "The Curious Case of the Pancake Tower.....Think of a posted of the last supper with a giant cartoon bowl of meatballs on the table....nothing is off the table. We just need our customers to look at it and chuckle, laugh or think...
It is a fast food type place and the logo is red and yellow. I uploaded a color scheme but don't feel you are limited to just that. It is just a guide.
Target Market(s)
Blue collar workers, college kids,
Industry/Entity Type
Movie
Requirements
Must have
- It has to be fun and quirky but not too offensive or inappropriate
Nice to have
- Look at the color scheme I uploaded...I like the idea of doing it cartoon "like"
Should not have
- No Porn....abusive etc...

```html
<!DOCTYPE html>
<html lang="en">
<head>
<meta charset="utf-8">
<title>Orvin's Legendary Slider Shack – Meatball Poster</title>
<link rel="stylesheet" href="https://fonts.googleapis.com/css2?family=Bebas+Neue&family=Yellowtail&family=Poiret+One&display=swap">
<style>
  :root {
    --page: #ffffff;
    --poster-light: #fcd53a;
    --poster-mid: #f6bd14;
    --poster-edge: #e6a20c;
    --ink: #454e50;
    --highlight: #ffffff;
    --definition: #e8321e;
    --rule: #2b2e2f;
  }
  html, body {
    margin: 0;
    padding: 0;
    width: 1200px;
    height: 900px;
    overflow: hidden;
    background: var(--page);
  }
  .canvas {
    position: relative;
    width: 1200px;
    height: 900px;
  }
  .poster {
    position: absolute;
    left: 289px;
    top: 47px;
    width: 550px;
    height: 806px;
    background: radial-gradient(ellipse at 45% 40%, var(--poster-light) 0%, var(--poster-mid) 60%, var(--poster-edge) 100%);
    box-shadow: 0 0 3px rgba(0,0,0,0.35);
    overflow: hidden;
  }
  .frame-marks {
    position: absolute;
    left: 0;
    top: 0;
  }
  .wordmark {
    position: absolute;
    left: 0;
    width: 100%;
    margin: 0;
    text-align: center;
    color: var(--ink);
    line-height: 1;
  }
  .wordmark--block {
    font-family: "Bebas Neue", "Arial Narrow", sans-serif;
    font-weight: 400;
    letter-spacing: 1px;
    text-shadow: -3px 3px 0 var(--highlight);
  }
  .wordmark--script {
    font-family: "Yellowtail", cursive;
    font-weight: 400;
  }
  .wordmark--owner { top: 8px; font-size: 160px; }
  .wordmark--legendary { top: 140px; font-size: 52px; }
  .wordmark--slider { top: 182px; font-size: 154px; }
  .wordmark--shack { top: 328px; font-size: 58px; }
  .definition {
    position: absolute;
    left: 5px;
    top: 470px;
    width: 540px;
    color: var(--definition);
    font-family: "Poiret One", "Century Gothic", sans-serif;
    font-weight: 400;
  }
  .definition__term {
    margin: 0 0 38px 0;
    font-size: 30px;
    letter-spacing: 0.5px;
  }
  .definition__senses {
    margin: 0;
    padding-left: 30px;
    font-size: 25px;
    line-height: 31px;
  }
</style>
</head>
<body>
<div class="canvas">
  <article class="poster">
    <svg class="frame-marks" width="550" height="806" viewBox="0 0 550 806" aria-hidden="true">
      <g fill="none" stroke="var(--rule)" stroke-width="5">
        <polyline points="25,60 25,20 91,20"/>
        <polyline points="459,20 525,20 525,60"/>
      </g>
      <circle cx="41" cy="418" r="17" fill="var(--rule)"/>
      <circle cx="512" cy="418" r="17" fill="var(--rule)"/>
      <rect x="104" y="413" width="340" height="7" fill="var(--rule)"/>
    </svg>

    <h1 class="wordmark wordmark--block wordmark--owner">Orvin’s</h1>
    <p class="wordmark wordmark--script wordmark--legendary">Legendary</p>
    <p class="wordmark wordmark--block wordmark--slider">Slider</p>
    <p class="wordmark wordmark--script wordmark--shack">Shack</p>

    <section class="definition">
      <p class="definition__term">meat·ball &nbsp;(mtbôl)</p>
      <ol class="definition__senses">
        <li>A small ball of ground meat<br>variously seasoned and cooked.</li>
        <li>Slang A stupid, clumsy, or dull person.</li>
      </ol>
    </section>
  </article>
</div>
</body>
</html>
```